Meridel Advisory & Coaching Collective Web Site Design

Help!

We have started designing and building a Web site to promote and sell training services to HR managers. But we are not very good designers. In fact, we stink.

We have a logo.

We have most of the content (more or less) and the site architecture. But we have put together a pretty lousy look and feel.

Take a look: http://brightlowpath.example/vortalindex.html

What we'd like is a Web 3.0 type design - clean, simple, modern looking. Some sites we admire:

pinvale.example
trelosk.example
skivorn.example
quibbledot.example
morpa.example

We have access to stock photography, some of which we've used on the site we've built so far. You can use those and others. But keep it simple.

Target Market(s)

Professional HR managers in larger companies

Requirements
Must have
• Use our logo and a color scheme based off of it. Logo file uploaded.

Need to see home page and examples of secondary pages, based on site currently online.

```html
<!DOCTYPE html>
<html lang="en">
<head>
<meta charset="utf-8">
<title>Cohortwise — Generational Tools &amp; Training for HR Professionals</title>
<link rel="stylesheet" href="https://fonts.googleapis.com/css2?family=Ubuntu:ital,wght@0,300;0,400;0,500;0,700;1,400&family=Open+Sans:wght@400;600;700&family=Gentium+Book+Plus:ital@1&display=swap">
<style>
:root{
  --ink:#333437;
  --ink-soft:#555;
  --bar:#2f3033;
  --band:#333438;
  --link:#2556b8;
  --brand-blue:#1d4ba8;
  --brand-red:#d4282c;
  --brand-orange:#f39a2b;
  --brand-green:#7cc242;
  --sky-top:#8fcde9;
  --sky-mid:#cfe9f5;
  --rule:#d9d9d9;
}
*{box-sizing:border-box;margin:0;padding:0}
html,body{width:1200px;height:857px;overflow:hidden;background:#fff}
body{position:relative;font-family:"Ubuntu",sans-serif;color:var(--ink)}
a{text-decoration:none;color:inherit}

.top-bar{position:absolute;left:0;top:0;width:1200px;height:30px;background:var(--bar);color:#fff}
.top-bar .tagline{position:absolute;left:194px;top:7px;font:600 12px "Open Sans",sans-serif;letter-spacing:.1px}
.top-bar .tagline em{font:italic 12px "Gentium Book Plus",serif;color:var(--brand-orange)}
.top-bar .util{position:absolute;left:686px;top:9px;font:400 11px "Open Sans",sans-serif;display:flex;gap:16px}
.top-bar .social{position:absolute;left:876px;top:6px;font:700 14px "Ubuntu",sans-serif;display:flex;gap:25px}

.site-header{position:absolute;left:0;top:30px;width:1200px;height:80px;
  background:repeating-linear-gradient(135deg,#fafafa 0 2px,#f2f2f2 2px 4px)}
.brand{position:absolute;left:190px;top:25px;display:flex;align-items:center;gap:10px}
.brand .dot{width:26px;height:26px;border-radius:50%;background:var(--brand-blue)}
.brand .name{font:400 23px "Ubuntu",sans-serif;color:var(--ink)}
.main-nav{position:absolute;left:516px;top:32px;display:flex;gap:19px;font:500 12px "Open Sans",sans-serif;color:var(--ink)}
.main-nav .current{color:var(--link)}

.hero{position:absolute;left:0;top:110px;width:1200px;height:272px;
  background:radial-gradient(ellipse at 30% 70%,#fff 0,rgba(255,255,255,.6) 30%,transparent 60%),
  radial-gradient(ellipse at 85% 40%,#eef8fc 0,transparent 45%),
  linear-gradient(180deg,var(--sky-top) 0%,var(--sky-mid) 55%,#e9f5fa 100%)}
.hero .photo{position:absolute;left:318px;top:16px;width:160px;height:256px;border-radius:4px;
  background:linear-gradient(180deg,rgba(200,190,178,.35) 0%,rgba(176,168,156,.75) 45%,rgba(160,152,142,.9) 100%)}
.hero .arrow{position:absolute;top:102px}
.hero .arrow.prev{left:188px}
.hero .arrow.next{left:984px}
.hero h1{position:absolute;left:575px;top:58px;font-weight:400;color:var(--ink);white-space:nowrap}
.hero h1 .the{font:italic 23px "Gentium Book Plus",serif}
.hero h1 .big{font:300 54px "Ubuntu",sans-serif;color:var(--brand-red);letter-spacing:-1px}
.hero h1 .gen{font:400 24px "Ubuntu",sans-serif}
.hero p{position:absolute;left:576px;top:124px;width:368px;font:400 12px/20.5px "Ubuntu",sans-serif;color:var(--ink)}
.hero .cta{position:absolute;left:576px;top:198px;width:322px;height:32px;border-radius:16px;
  background:linear-gradient(#fff,#e8e8e8);border:1px solid #cfd3d6;box-shadow:0 1px 2px rgba(0,0,0,.15);
  font:400 14px/30px "Ubuntu",sans-serif;padding-left:17px;color:var(--ink)}

.feature-band{position:absolute;left:0;top:382px;width:1200px;height:113px;background:var(--band)}
.card{position:absolute;top:10px;width:257px;height:93px;background:linear-gradient(90deg,#fff,#e9e9e9);overflow:hidden}
.card .people{position:absolute;left:0;top:0;width:102px;height:90px;background:linear-gradient(180deg,#d8d8d8,#4a4c52)}
.card .label{position:absolute;right:36px;top:26px;text-align:right;font:300 19px/21px "Ubuntu",sans-serif;color:#444}
.card .tab{position:absolute;right:0;top:31px;width:22px;height:32px;display:flex;align-items:center;justify-content:center}
.card .underline{position:absolute;left:0;bottom:0;width:100%;height:3px}
.card.c1{left:198px}.card.c1 .tab{background:var(--brand-orange)}.card.c1 .underline{background:linear-gradient(90deg,var(--brand-orange),#fde6c8)}
.card.c2{left:471px}.card.c2 .tab{background:var(--brand-red)}.card.c2 .underline{background:linear-gradient(90deg,var(--brand-red),#f6cccc)}
.card.c3{left:747px}.card.c3 .tab{background:var(--brand-green)}.card.c3 .underline{background:linear-gradient(90deg,var(--brand-green),#dcefc9)}

.mission{position:absolute;left:188px;top:512px;font:300 17px "Ubuntu",sans-serif;color:var(--ink)}
.more{position:absolute;left:879px;top:513px;font:400 14px "Ubuntu",sans-serif;color:var(--link);display:flex;align-items:center;gap:8px}

.services{position:absolute;left:200px;top:560px;width:800px;height:80px}
.service{position:absolute;top:0;width:200px}
.service .icon{position:absolute;left:12px;top:1px;width:36px;height:36px;border-radius:50%;background:radial-gradient(circle at 40% 35%,#3f74cf,var(--brand-blue) 70%);display:flex;align-items:center;justify-content:center}
.service .shadow{position:absolute;left:0;top:36px;width:48px;height:4px;border-radius:50%;background:radial-gradient(rgba(0,0,0,.25),transparent 70%)}
.service h2{position:absolute;left:60px;top:8px;font:400 17px "Ubuntu",sans-serif;color:var(--ink)}
.service p{position:absolute;left:62px;top:36px;width:110px;font:400 10px/14px "Open Sans",sans-serif;color:var(--ink)}

.rule{position:absolute;left:193px;width:823px;height:1px;background:var(--rule)}
.clients-title{position:absolute;left:199px;top:711px;font:400 15.5px/16px "Ubuntu",sans-serif;color:var(--ink)}
.clients-arrow{position:absolute;left:320px;top:711px}
.clients{position:absolute;left:407px;top:708px;width:585px;height:40px;display:flex;align-items:center;justify-content:space-between;color:#6b6b6b}
.clients span{font:500 17px "Ubuntu",sans-serif}

.site-footer .copy{position:absolute;left:191px;top:801px;font:400 10px "Open Sans",sans-serif;color:var(--ink)}
.site-footer nav{position:absolute;left:456px;top:800px;display:flex;gap:16px;font:400 11px "Open Sans",sans-serif;color:var(--link)}
</style>
</head>
<body>

<div class="top-bar">
  <div class="tagline">Generational Tools &amp; Training <em>for</em> HR Professionals</div>
  <nav class="util"><a href="#">Home</a><a href="#">About Us</a><a href="#">Contact</a></nav>
  <div class="social"><a href="#">Friendlane</a><a href="#">Chirpline</a></div>
</div>

<header class="site-header">
  <div class="brand"><span class="dot"></span><span class="name">Cohortwise</span></div>
  <nav class="main-nav">
    <a class="current" href="#">Home</a><a href="#">Gen 101</a><a href="#">Gen Gaps</a><a href="#">Strategies</a>
    <a href="#">Resources</a><a href="#">Training</a><a href="#">Tools</a><a href="#">Discuss</a>
  </nav>
</header>

<section class="hero">
  <div class="photo" role="img" aria-label="Photo of a smiling senior businessman in a grey suit with arms crossed"></div>
  <svg class="arrow prev" width="24" height="48" viewBox="0 0 24 48"><path d="M22 2 2 24l20 22" fill="none" stroke="#333" stroke-width="1.8"/></svg>
  <svg class="arrow next" width="24" height="48" viewBox="0 0 24 48"><path d="M2 2l20 22L2 46" fill="none" stroke="#333" stroke-width="1.8"/></svg>
  <h1><span class="the">the</span> <span class="big">Silent</span> <span class="gen">Generation</span></h1>
  <p>The hardship of the Great Depression, the shared sacrifice of total war during World War II, and the struggle against interna&shy;tional communism shaped the Silent Generation.</p>
  <a class="cta" href="#">Learn more about the Different Generations</a>
</section>

<section class="feature-band">
  <a class="card c1" href="#">
    <div class="people" role="img" aria-label="Photo of two businessmen in suits"></div>
    <div class="label">Generations<br>101</div>
    <div class="tab"><svg width="10" height="20" viewBox="0 0 10 20"><path d="M1 1l8 9-8 9" fill="none" stroke="#fff" stroke-width="1.4"/></svg></div>
    <div class="underline"></div>
  </a>
  <a class="card c2" href="#">
    <div class="people" role="img" aria-label="Photo of a businesswoman and a businessman"></div>
    <div class="label">Generation<br>Gaps</div>
    <div class="tab"><svg width="10" height="20" viewBox="0 0 10 20"><path d="M1 1l8 9-8 9" fill="none" stroke="#fff" stroke-width="1.4"/></svg></div>
    <div class="underline"></div>
  </a>
  <a class="card c3" href="#">
    <div class="people" role="img" aria-label="Photo of a senior businessman and a businesswoman"></div>
    <div class="label">Generation<br>Strategies</div>
    <div class="tab"><svg width="10" height="20" viewBox="0 0 10 20"><path d="M1 1l8 9-8 9" fill="none" stroke="#fff" stroke-width="1.4"/></svg></div>
    <div class="underline"></div>
  </a>
</section>

<p class="mission">Cohortwise is committed to providing HR professionals with training that matters.</p>
<a class="more" href="#">tell me more
  <svg width="22" height="12" viewBox="0 0 22 12"><path d="M0 6h20M15 1l5 5-5 5" fill="none" stroke="var(--brand-orange)" stroke-width="1.3"/></svg></a>

<section class="services">
  <div class="service" style="left:0">
    <div class="shadow"></div>
    <div class="icon"><svg width="18" height="20" viewBox="0 0 18 20"><rect x="5" y="1" width="11" height="14" rx="1" fill="none" stroke="#fff" stroke-width="1.8"/><path d="M2 5v13h10" fill="none" stroke="#fff" stroke-width="1.8"/></svg></div>
    <h2>Resources</h2><p>What makes our trainings so much better than the rest.</p>
  </div>
  <div class="service" style="left:210px">
    <div class="shadow"></div>
    <div class="icon"><svg width="16" height="22" viewBox="0 0 16 22"><path d="M10 1 2 13h6l-2 8 8-12H8z" fill="#fff"/></svg></div>
    <h2>Training</h2><p>What makes our trainings so much better than the rest.</p>
  </div>
  <div class="service" style="left:412px">
    <div class="shadow"></div>
    <div class="icon"><svg width="20" height="20" viewBox="0 0 20 20"><path d="M3 17 17 3M3 3l14 14" stroke="#fff" stroke-width="2.6" stroke-linecap="round"/></svg></div>
    <h2>Tools</h2><p>What makes our trainings so much better than the rest.</p>
  </div>
  <div class="service" style="left:620px">
    <div class="shadow"></div>
    <div class="icon"><svg width="22" height="18" viewBox="0 0 22 18"><ellipse cx="12" cy="7" rx="9" ry="6" fill="#fff"/><path d="M6 11 3 16l7-4z" fill="#fff"/></svg></div>
    <h2>Discuss</h2><p>What makes our trainings so much better than the rest.</p>
  </div>
</section>

<div class="rule" style="top:680px"></div>
<h3 class="clients-title">Companies<br>We Work With</h3>
<svg class="clients-arrow" width="16" height="34" viewBox="0 0 16 34"><path d="M1 1l14 16L1 33" fill="none" stroke="var(--brand-red)" stroke-width="1.4"/></svg>
<div class="clients">
  <span>Tarnbrook</span><span>Velmont Financial</span><span>Quarrelo</span><span>Halden &amp; Halden</span>
</div>
<div class="rule" style="top:774px"></div>

<footer class="site-footer">
  <p class="copy">Copyright 2011, Oxbel Research</p>
  <nav>
    <a href="#">Home</a><a href="#">Gen 101</a><a href="#">Gen Gaps</a><a href="#">Strategies</a><a href="#">Resources</a>
    <a href="#">Training</a><a href="#">Tools</a><a href="#">Discuss</a><a href="#">About</a><a href="#">Contact</a>
  </nav>
</footer>

</body>
</html>
```